New CI for Powerpoint Catalogue & Stationary

We are selling premium promotional gifts made of
- nuts, chocolate, -> mainly for christmans
- icecreampowder and BBQ Rubs -> mainly for summer.

We need a new design for our powerpoint catalogue & stationary.

In order to highlight our sustainabilty approach, we deceided to go for the colors green, brown & white. I am happy with that choice but I want a new look.

We are building a new website under brovika.de/cms.

The final design should communicate sustainabilty, premium quality and delicious products.

Target Market(s)

Companies looking for a premium gift for the clients or employees

Font styles to use
Other font styles liked:
• Memphis

```html
<!DOCTYPE html>
<html lang="de">
<head>
<meta charset="utf-8">
<title>Brovika – Visitenkarte</title>
<link href="https://fonts.googleapis.com/css2?family=Arvo:wght@400;700&display=swap" rel="stylesheet">
<style>
  :root{
    --stage:#9a9a9a;
    --kraft:#c9a57a;
    --kraft-text:#d8b88e;
    --brown:#6e3a2e;
    --green:#5cbc45;
    --white:#ffffff;
  }
  *{box-sizing:border-box;margin:0;padding:0}
  html,body{width:1200px;height:862px;overflow:hidden;background:var(--stage);font-family:"Arvo",Georgia,serif}
  .stage{position:relative;width:1200px;height:862px}
  .card{position:absolute;top:263px;width:520px;height:336px;background:var(--kraft);box-shadow:0 10px 24px rgba(0,0,0,.25)}
  .card--front{left:50px}
  .card--back{left:630px}
  .panel{position:absolute;left:34px;right:34px;top:30px;bottom:30px;background:var(--brown)}
  .band{position:absolute;left:34px;right:34px;background:var(--green)}
  .card--front .band{top:98px;height:84px}
  .card--back .band{top:86px;height:96px}

  .badge{position:absolute;left:50%;top:140px;width:178px;height:178px;margin:-89px 0 0 -89px;border-radius:50%;background:var(--white);display:flex;align-items:center;justify-content:center}
  .badge__name{font-size:34px;font-weight:400;color:var(--brown);letter-spacing:1px}

  .person{position:absolute;left:64px;top:38px;color:var(--green)}
  .person__name{font-size:22px;font-weight:700}
  .person__role{font-size:13px;margin-top:2px}

  .contacts{position:absolute;top:100px;left:58px;right:58px;display:flex;justify-content:space-between;color:var(--brown);font-size:13px}
  .contacts ul{list-style:none}
  .contacts li{display:flex;align-items:center;gap:10px;height:30px}
  .contacts svg{width:18px;height:18px;flex:none}

  .address{position:absolute;left:64px;top:206px;color:var(--kraft-text);font-size:14px;line-height:1.45}
</style>
</head>
<body>
<main class="stage">
  <section class="card card--front" aria-label="Vorderseite">
    <div class="panel"></div>
    <div class="band"></div>
    <div class="badge"><span class="badge__name">Brovika</span></div>
  </section>

  <section class="card card--back" aria-label="Rückseite">
    <div class="panel"></div>
    <div class="band"></div>
    <div class="person">
      <p class="person__name">Jonas Wendler</p>
      <p class="person__role">Gründer und Geschäftsführer</p>
    </div>
    <div class="contacts">
      <ul>
        <li>
          <svg viewBox="0 0 20 20" aria-hidden="true"><circle cx="10" cy="10" r="10" fill="#fff"/><path d="M6.5 5.5l2 0 1 2.5-1.2 1a6 6 0 0 0 2.7 2.7l1-1.2 2.5 1 0 2c-5 .5-8.5-3-8-8z" fill="var(--green)"/></svg>
          +49 (0) 40 51 76 408-10
        </li>
        <li>
          <svg viewBox="0 0 20 20" aria-hidden="true"><rect x="5" y="2" width="10" height="5" fill="#fff"/><rect x="2" y="7" width="16" height="7" rx="1.5" fill="#fff"/><rect x="5" y="12" width="10" height="6" fill="#fff" stroke="var(--green)"/></svg>
          +49 (0) 51 76 408-12
        </li>
      </ul>
      <ul>
        <li>
          <svg viewBox="0 0 20 20" aria-hidden="true"><rect x="2" y="5" width="16" height="11" fill="#fff"/><path d="M2 5l8 6 8-6" fill="none" stroke="var(--green)" stroke-width="1.4"/></svg>
          j.wendler@brovika.de
        </li>
        <li>
          <svg viewBox="0 0 20 20" aria-hidden="true" fill="none" stroke="#fff" stroke-width="1.4"><circle cx="10" cy="10" r="8"/><ellipse cx="10" cy="10" rx="3.5" ry="8"/><path d="M2 10h16M3.5 6h13M3.5 14h13"/></svg>
          www.brovika.de
        </li>
      </ul>
    </div>
    <p class="address">Brovika Premium Snacks GmbH<br>Lindenallee 14 22301 Hamburg</p>
  </section>
</main>
</body>
</html>
```